New Church Plant website for Brightvale Church

I would like a six page website designed that is clean and easy to navigate. The six pages will include (1) About Us (2) Home (3) Contact Us (4) Sermons (5) Donate (6) Ministries. There will be subcategories for each category as well. The color scheme can be found in the attached magazine of Brightvale. Much of the information found in the booklet will be used on the website. I would love to see a design that pops but still clean and easy to navigate. I have included a good deal of pictures for the creative. Please see the current website at brightvalechapel.example which is temporary as we are preparing for a launch. I would now like to create a long-term site.

Target Market(s)

People interested in Christian church

Number of Pages Required

5+ page

Font styles to use
Sans Serif

Colors
ffffff
f78f20

Requirements
Must have
• a site that pops but is clean and easy to navigate.

```html
<!DOCTYPE html>
<html lang="en">
<head>
<meta charset="utf-8">
<title>Brightvale Church</title>
<link href="https://fonts.googleapis.com/css2?family=Montserrat:wght@300;400;500;600;700;800&display=swap" rel="stylesheet">
<style>
:root{
  --orange:#f07a1f;
  --orange-deep:#e8661a;
  --orange-light:#f78f20;
  --white:#ffffff;
  --ink:#2a2a2a;
  --text:#3c3c3c;
  --paper:#e4e2e1;
  --dark:#141414;
  --navy:#1b2232;
  --frame:#1e1e1e;
}
*{box-sizing:border-box;margin:0;padding:0}
html,body{width:1200px;height:4277px;overflow:hidden}
body{position:relative;font-family:'Montserrat',sans-serif;background:var(--paper);color:var(--text)}
.abs{position:absolute}
.center{text-align:center;left:0;width:1200px}

/* hero */
.hero{position:absolute;left:0;top:0;width:1200px;height:880px;overflow:hidden}
.hero-photo{position:absolute;inset:0;background:radial-gradient(ellipse at 50% 40%,#5a524c 0%,#2e2a28 50%,#111 100%)}
.hero-shade{position:absolute;left:0;top:600px;width:1200px;height:280px;background:linear-gradient(#1a1a1a00,#0d0d0dcc)}
.brand{position:absolute;left:120px;top:62px;display:flex;align-items:center;gap:10px}
.brand-mark{width:22px;height:22px;border-radius:50%;background:var(--orange)}
.brand-name{font-size:28px;font-weight:600;color:var(--white)}
.nav{position:absolute;top:84px;left:510px;display:flex;gap:32px;font-size:12px;font-weight:500;color:var(--white)}
.btn{position:absolute;display:flex;align-items:center;justify-content:center;background:var(--orange);color:var(--white);font-size:12px;font-weight:600;border-radius:20px}
.hero-quote{position:absolute;left:360px;top:280px;width:480px;height:118px;border:2px solid var(--white);border-radius:14px;display:flex;align-items:center;justify-content:center;text-align:center;color:var(--white);font-size:24px;line-height:29px}
.qmark{position:absolute;font-size:40px;font-weight:700;line-height:1;color:var(--white);padding:0 6px}
.launch{top:742px;font-size:40px;font-weight:800;letter-spacing:9px;color:var(--orange)}
.launch b{color:var(--white);font-weight:800}
.launch-sub{top:794px;font-size:13px;font-weight:600;letter-spacing:3px;color:var(--white)}

/* content sections */
.photo{position:absolute}
.frame{position:absolute;border:8px solid var(--frame)}
.h-big{font-size:38px;font-weight:600;color:var(--orange)}
.h-sub{font-size:24px;font-weight:500;color:var(--ink)}
.body-copy{position:absolute;font-size:11px;line-height:19px;color:var(--text);text-align:justify}
.body-copy p+p{margin-top:14px}
.list{position:absolute;left:120px;top:2010px;width:400px;list-style:none;font-size:14px;line-height:24px;color:var(--text)}
.list li{position:relative;padding-left:40px;margin-bottom:24px;text-align:justify}
.list li svg{position:absolute;left:0;top:6px}

.quote-band{position:absolute;left:0;top:2512px;width:1200px;height:278px;background:linear-gradient(90deg,#2a2320 0%,var(--navy) 40%,#141a26 100%)}
.quote-box{position:absolute;left:120px;top:2592px;width:960px;height:118px;border:2px solid var(--white);border-radius:14px;display:flex;align-items:center;justify-content:center;text-align:center;color:var(--white);font-size:24px;line-height:29px}

.mission-band{position:absolute;left:0;top:3515px;width:1200px;height:200px;background:linear-gradient(90deg,var(--orange-deep),var(--orange-light))}
.mission-title{top:3496px;font-size:36px;font-weight:800;letter-spacing:8px;color:var(--ink)}
.mission-text{top:3593px;font-size:24px;line-height:30px;color:var(--white)}

.involve{position:absolute;left:0;top:3715px;width:1200px;height:562px;background:radial-gradient(ellipse at 50% 80%,#3a3a3a 0%,#1a1a1a 60%,#0c0c0c 100%)}
.pill{position:absolute;left:280px;width:240px;height:38px;border:2px solid var(--white);border-radius:20px;color:var(--white);font-size:12px;font-weight:600;display:flex;align-items:center;padding-left:40px}
.pill::before{content:"";position:absolute;left:20px;top:14px;width:6px;height:6px;border-right:1.5px solid var(--white);border-top:1.5px solid var(--white);transform:rotate(45deg)}
.bullet{position:absolute;left:300px;font-size:12px;color:var(--white);padding-left:20px}
.bullet::before{content:"";position:absolute;left:0;top:5px;width:5px;height:5px;border-right:1.5px solid var(--white);border-top:1.5px solid var(--white);transform:rotate(45deg)}
.divider{position:absolute;left:599px;top:3880px;width:1px;height:190px;background:#777}
.or{position:absolute;left:580px;top:3955px;width:40px;height:40px;border-radius:50%;background:var(--white);color:var(--ink);font-size:11px;font-weight:700;display:flex;align-items:center;justify-content:center}
.pay-card{position:absolute;top:4034px;width:26px;height:18px;border:1.5px solid var(--white);border-radius:3px}
.foot-line{position:absolute;left:120px;top:4150px;width:960px;height:1px;background:#555}
</style>
</head>
<body>

<!-- HERO -->
<section class="hero">
  <div class="hero-photo" role="img" aria-label="Congregation seated in a church sanctuary facing the altar"></div>
  <div class="hero-shade"></div>
  <svg class="abs" style="left:0;top:520px" width="1200" height="170" viewBox="0 0 1200 170">
    <defs>
      <linearGradient id="band" x1="0" x2="1" y1="0" y2="0">
        <stop offset="0" stop-color="#e8661a"/>
        <stop offset="0.45" stop-color="#fbe3cf"/>
        <stop offset="0.55" stop-color="#fbe3cf"/>
        <stop offset="1" stop-color="#e8661a"/>
      </linearGradient>
    </defs>
    <polygon points="0,20 600,150 1200,20 1200,80 600,160 0,80" fill="url(#band)"/>
    <polygon points="0,80 600,160 1200,80 1200,90 600,162 0,90" fill="#1a1a1a" opacity="0.5"/>
  </svg>

  <div class="brand"><span class="brand-mark"></span><span class="brand-name">Brightvale</span></div>
  <nav class="nav"><span>Home</span><span>About</span><span>Sermons</span><span>Ministries</span><span>Faq's</span><span>Contact</span></nav>
  <div class="btn" style="left:968px;top:73px;width:112px;height:40px">Donate</div>

  <div class="hero-quote">Flourishing people planting<br>flourishing churches</div>
  <div class="qmark" style="left:378px;top:262px;background:#3a3532">“</div>
  <div class="qmark" style="left:778px;top:384px;background:#3a3532">”</div>

  <div class="abs center launch">LAUNCHING <b>APRIL 12,</b> 2020</div>
  <div class="abs center launch-sub">"A MULTI-ETHNIC CHURCH PLANTING CHURCH"</div>

  <svg class="abs" style="left:455px;top:836px" width="290" height="44" viewBox="0 0 290 44" fill="#ffffff">
    <g><rect x="13" y="8" width="2" height="8"/><rect x="10" y="10" width="8" height="2"/><polygon points="14,16 6,26 22,26"/><rect x="7" y="26" width="14" height="14"/></g>
    <g transform="translate(55 0)"><rect x="13" y="8" width="2" height="8"/><rect x="10" y="10" width="8" height="2"/><polygon points="14,16 6,26 22,26"/><rect x="7" y="26" width="14" height="14"/></g>
    <g transform="translate(118 0)"><rect x="25" y="0" width="3" height="10"/><rect x="21" y="3" width="11" height="3"/><polygon points="26,10 2,30 50,30"/><rect x="6" y="30" width="40" height="12"/></g>
    <g transform="translate(205 0)"><rect x="13" y="8" width="2" height="8"/><rect x="10" y="10" width="8" height="2"/><polygon points="14,16 6,26 22,26"/><rect x="7" y="26" width="14" height="14"/></g>
    <g transform="translate(260 0)"><rect x="13" y="8" width="2" height="8"/><rect x="10" y="10" width="8" height="2"/><polygon points="14,16 6,26 22,26"/><rect x="7" y="26" width="14" height="14"/></g>
  </svg>
</section>

<!-- ABOUT THE PLANTER -->
<section>
  <div class="frame" style="left:180px;top:975px;width:360px;height:440px"></div>
  <div class="photo" role="img" aria-label="Portrait of the church planter in an orange sweater" style="left:130px;top:935px;width:460px;height:525px;background:radial-gradient(ellipse at 50% 55%,#8a5a3c 0%,#5a3420 45%,#e8661a 80%,#e4e2e100 100%);border-radius:38% 45% 40% 50%"></div>
  <div class="abs" style="left:680px;top:1035px;font-size:40px;color:var(--ink);font-weight:300">I'm <span style="color:var(--orange);font-weight:800;letter-spacing:5px">MARCUS</span></div>
  <div class="abs" style="left:680px;top:1084px;font-size:14px;color:var(--ink)">Church Planter</div>
  <div class="body-copy" style="left:680px;top:1122px;width:400px">Marcus Hale was born and raised as a preacher's kid in the central city of Riverton. As a youth, he was involved with gangs and by the age of 22, was a successful drug dealer. After a near death experience, he gave his life to Jesus and would later become an ordained minister. In 2005, he planted his first church in the central city of Riverton. In 2016, he led the launch of a north side multi-ethnic ministry initiative for cornerstone church. He and his wife Jo-Ann are the proud parents of 5 adult children and the proud grandparents of 10.</div>
  <div class="btn" style="left:680px;top:1310px;width:112px;height:38px">My Story</div>
</section>

<div class="photo" role="img" aria-label="Church members of different generations smiling together around an open Bible" style="left:0;top:1508px;width:1200px;height:279px;background:linear-gradient(90deg,#3a2e28,#6a5448 35%,#4a3a32 60%,#2a2420)"></div>

<!-- COMMUNITY -->
<section>
  <div class="abs center h-big" style="top:1843px">Community</div>
  <div class="abs center h-sub" style="top:1888px">Involvement</div>
  <ul class="list">
    <li><svg width="20" height="12" viewBox="0 0 20 12"><polyline points="2,6 7,10 18,2" fill="none" stroke="#f07a1f" stroke-width="2"/></svg>Board member of Neighborhood Supply House and Allies in Hope</li>
    <li><svg width="20" height="12" viewBox="0 0 20 12"><polyline points="2,6 7,10 18,2" fill="none" stroke="#f07a1f" stroke-width="2"/></svg>Board member of Northgate High School</li>
    <li><svg width="20" height="12" viewBox="0 0 20 12"><polyline points="2,6 7,10 18,2" fill="none" stroke="#f07a1f" stroke-width="2"/></svg>Member of steering council of Meridian Health Care</li>
    <li><svg width="20" height="12" viewBox="0 0 20 12"><polyline points="2,6 7,10 18,2" fill="none" stroke="#f07a1f" stroke-width="2"/></svg>Founder and President of Common Ground, a neighborhood development organization</li>
    <li><svg width="20" height="12" viewBox="0 0 20 12"><polyline points="2,6 7,10 18,2" fill="none" stroke="#f07a1f" stroke-width="2"/></svg>President of the Riverton Covenant, a group of multi-ethnic pastors from southeastern Lakeland who stand as one in promoting racial unity within the body of Christ</li>
  </ul>
  <div class="frame" style="left:660px;top:1960px;width:360px;height:437px"></div>
  <div class="photo" role="img" aria-label="Hands joined in prayer over an open Bible" style="left:615px;top:1925px;width:460px;height:520px;background:radial-gradient(ellipse at 55% 50%,#5a6a88 0%,#8a7a74 45%,#c8c0bc 75%,#e4e2e100 100%);border-radius:42% 40% 45% 38%"></div>
</section>

<!-- QUOTE -->
<section>
  <div class="quote-band"></div>
  <div class="photo" role="img" aria-label="Pastor speaking on stage" style="left:90px;top:2512px;width:230px;height:278px;background:linear-gradient(#3a2a24,#8a4a30 60%,#5a3426)"></div>
  <div class="quote-box">I value multi-ethnic ministry because I am a product of what<br>can happen through multi-ethnic relationships.</div>
  <div class="qmark" style="left:138px;top:2574px;background:#5a3a2c">“</div>
  <div class="qmark" style="left:1018px;top:2696px;background:#161c28">”</div>
  <div class="abs center" style="top:2743px;font-size:14px;font-weight:600;color:var(--orange)">- Marcus Hale -</div>
</section>

<!-- CHURCH -->
<section>
  <div class="abs center h-big" style="top:2848px">Brightvale</div>
  <div class="abs center h-sub" style="top:2893px">Church</div>
  <div class="frame" style="left:180px;top:2965px;width:360px;height:435px"></div>
  <div class="photo" role="img" aria-label="Stone cross against a cloudy sky in black and white" style="left:125px;top:2935px;width:465px;height:515px;background:radial-gradient(ellipse at 50% 50%,#3a3a3a 0%,#8a8a8a 45%,#d8d8d8 75%,#e4e2e100 100%);border-radius:40% 45% 42% 40%"></div>
  <div class="body-copy" style="left:680px;top:3008px;width:400px">
    <p>The church planting scene Riverton's central city is problematic and serves as an indictment on both the black and white church. Black churches are not raising up and supporting indigenous church planters outside of the "multi-site" model. Conversely white churches plant churches with "outside" ministers, failing to embrace the central city context and culture and misunderstanding the need for multi-ethnic leadership and decision making.</p>
    <p>Without the presence of contextually-appropriate, bible-based church plants, many people in Riverton are leaving traditional churches and transitioning to nothing.</p>
    <p>The gospel is under attack in Riverton. Multi-ethnic, contextually appropriate church plants are our counter-attack.</p>
  </div>
  <div class="btn" style="left:680px;top:3314px;width:112px;height:38px">Read More</div>
</section>

<!-- MISSION -->
<section>
  <div class="mission-band"></div>
  <div class="abs center mission-title">MISSION</div>
  <div class="abs center mission-text">To be a gospel-centered, multi-ethnic, church planting church built<br>on the pillars of Missions, Faith, Work &amp; Economics.</div>
</section>

<!-- GET INVOLVED -->
<section class="involve" role="img" aria-label="Worshippers with raised hands in black and white"></section>
<section>
  <div class="abs center" style="top:3768px;font-size:38px;font-weight:600;color:var(--orange)">Ways to</div>
  <div class="abs center" style="top:3815px;font-size:22px;font-weight:600;color:var(--white)">Get Involved Today:</div>
  <div class="pill" style="top:3900px">Join the Launch Team</div>
  <div class="pill" style="top:3957px">Sign up Today!</div>
  <div class="bullet" style="top:4033px">Pray</div>
  <div class="bullet" style="top:4061px">Give Sacrificially</div>
  <div class="divider"></div>
  <div class="or">OR</div>
  <div class="abs" style="left:680px;top:3895px;width:240px;font-size:11px;line-height:21px;color:var(--white)">Click <b>Donate</b> to give securely with a credit card through SecurePay</div>
  <div class="btn" style="left:680px;top:3955px;width:112px;height:38px">Donate</div>
  <div class="pay-card" style="left:682px"></div>
  <div class="pay-card" style="left:714px"></div>
  <div class="pay-card" style="left:746px"></div>
  <div class="pay-card" style="left:778px"></div>
  <div class="foot-line"></div>
  <div class="abs" style="left:120px;top:4208px;font-size:11px;color:var(--white)">Copyright © 2020 Brightvale Church.</div>
  <div class="abs" style="left:780px;top:4190px;width:300px;text-align:right;font-size:11px;color:var(--white)">For more information:</div>
  <div class="abs" style="left:780px;top:4207px;width:300px;text-align:right;font-size:15px;color:var(--white)">Call: <b>555 - 014 - 0191</b> or <b>Email Us</b></div>
</section>

</body>
</html>
```